Webdesign für Dienstleistung im Industriebereich
Zielgruppe
Dienstleistung im Industriebereich.
Siehe Word Dokument
Aufgabenstellung
Design der Tochterfirma www.kefa.tools berücksichtigen

```html
<!DOCTYPE html>
<html lang="de">
<head>
<meta charset="utf-8">
<title>Velto Systems – Services</title>
<link rel="stylesheet" href="https://fonts.googleapis.com/css2?family=Arimo:wght@400;700&family=Roboto+Condensed:wght@400;700&display=swap">
<style>
  :root {
    --red: #e0202e;
    --ink: #1e1e1e;
    --text: #333333;
    --muted: #7a7a7a;
    --nav: #555555;
    --header-top: #f4f4f4;
    --header-bottom: #dcdcdc;
    --card: #f7f7f7;
    --page: #e9e9e9;
    --white: #ffffff;
  }
  * { margin: 0; padding: 0; box-sizing: border-box; }
  html, body { width: 1200px; height: 801px; overflow: hidden; }
  body { background: var(--page); font-family: "Arimo", Arial, sans-serif; color: var(--text); position: relative; }

  .site-header {
    position: absolute; left: 0; top: 0; width: 1200px; height: 112px;
    background: linear-gradient(100deg, var(--header-top) 0%, #e6e6e6 45%, var(--header-bottom) 100%);
  }
  .brand { position: absolute; left: 150px; top: 32px; display: flex; align-items: center; gap: 12px; }
  .brand-mark { width: 44px; height: 44px; background: var(--red); }
  .brand-name { font-family: "Arimo", Arial, sans-serif; font-weight: 700; font-size: 27px; color: var(--red); line-height: 1; }

  .main-nav { position: absolute; left: 470px; top: 0; height: 112px; display: flex; align-items: flex-end; gap: 30px; padding-bottom: 26px; }
  .main-nav a { font-family: "Roboto Condensed", Arial, sans-serif; font-size: 21px; color: var(--nav); text-decoration: none; }
  .main-nav a.is-active {
    background: var(--red); color: var(--white); font-weight: 700;
    padding: 40px 12px 8px; margin-bottom: -8px;
  }

  .hero {
    position: absolute; left: 0; top: 112px; width: 1200px; height: 420px;
    background: linear-gradient(110deg, #6b3f24 0%, #a5683f 28%, #c99a6e 45%, #b9b9bd 62%, #e4e6ea 78%, #8e9096 100%);
  }
  .hero-title {
    position: absolute; left: 0; top: 128px; width: 1200px; text-align: center;
    font-family: "Roboto Condensed", Arial, sans-serif; font-weight: 700; font-size: 44px;
    color: var(--white); letter-spacing: 0.5px;
  }
  .hero-dots { position: absolute; left: 0; top: 208px; width: 1200px; display: flex; justify-content: center; gap: 6px; }
  .hero-dots span { width: 10px; height: 10px; border-radius: 50%; background: var(--white); }

  .services { position: absolute; left: 150px; top: 420px; display: flex; gap: 20px; }
  .service-card { width: 210px; height: 381px; background: var(--card); display: flex; flex-direction: column; }
  .service-body { padding: 18px 16px 0; height: 205px; }
  .service-title {
    font-family: "Roboto Condensed", Arial, sans-serif; font-weight: 700; font-size: 24px;
    color: var(--ink); text-align: center; line-height: 1.05; margin-bottom: 12px;
  }
  .service-text { font-size: 12px; line-height: 1.4; color: var(--text); }
  .service-more { display: block; margin-top: 14px; font-size: 11.5px; color: var(--muted); text-decoration: none; }
  .service-photo { flex: 1; margin-left: 30px; }
  .photo-montage { background: linear-gradient(135deg, #c9c7c2 0%, #6f6e6c 50%, #b8b5ad 100%); }
  .photo-logistik { background: linear-gradient(160deg, #8a5a4f 0%, #c48c78 45%, #e9c6a9 100%); }
  .photo-lager { background: linear-gradient(120deg, #5e5d58 0%, #c9a53a 45%, #8d8b84 100%); }
  .photo-beratung { background: linear-gradient(90deg, #e0781f 0%, #f29a3b 45%, #dcdad6 100%); }
</style>
</head>
<body>
  <header class="site-header">
    <div class="brand">
      <span class="brand-mark"></span>
      <span class="brand-name">Velto Systems</span>
    </div>
    <nav class="main-nav">
      <a href="#">Home</a>
      <a href="#">about</a>
      <a href="#">products</a>
      <a href="#" class="is-active">services</a>
      <a href="#">contact</a>
    </nav>
  </header>

  <section class="hero" role="img" aria-label="Geschwungene Metallfassade aus Kupfer- und Edelstahlplatten">
    <h1 class="hero-title">SERVICE AUF HÖCHSTEM NIVEAU.</h1>
    <div class="hero-dots"><span></span><span></span><span></span></div>
  </section>

  <main class="services">
    <article class="service-card">
      <div class="service-body">
        <h2 class="service-title">MONTAGE</h2>
        <p class="service-text">Kleben, schneiden, Sägen, Fügen, Clipsen oder kommissionieren. Wir verhelfen Ihnen zu Ihrem Ziel mit unserem spitzen Service.</p>
        <a class="service-more" href="#">...zusätzlicher Text</a>
      </div>
      <div class="service-photo photo-montage" role="img" aria-label="Trennschleifer bei der Metallbearbeitung"></div>
    </article>
    <article class="service-card">
      <div class="service-body">
        <h2 class="service-title">LOGISTIK</h2>
        <p class="service-text">Disposition der Bauteile, Frei Haus Lieferung der Ware oder eine gesamte Supplychain mit Finanzierung der Kaufteile. Wir bringen Sie an Ihr Ziel!</p>
        <a class="service-more" href="#">... zusätzlicher Text</a>
      </div>
      <div class="service-photo photo-logistik" role="img" aria-label="Containerschiff im Abendlicht"></div>
    </article>
    <article class="service-card">
      <div class="service-body">
        <h2 class="service-title">WARENAUSGABE AUTOMATEN</h2>
        <p class="service-text">Finanzierung, Leasing, Installation, Befüllung oder Betreuung wir unterstützen Sie!</p>
        <a class="service-more" href="#">... zusätzlicher Text</a>
      </div>
      <div class="service-photo photo-lager" role="img" aria-label="Lagerregale mit Warenausgabeautomaten"></div>
    </article>
    <article class="service-card">
      <div class="service-body">
        <h2 class="service-title">BERATUNG</h2>
        <p class="service-text">Einkaufsberatung mit Einstiegs­potentialanalyse, Industrie 4.0, mit Kanban, JIT und JIS Konzepte, Konsignationslagerkonzepte, Logistikberatung und Fracht­kostenreduktion.</p>
        <a class="service-more" href="#">...zusätzlicher Text</a>
      </div>
      <div class="service-photo photo-beratung" role="img" aria-label="Berater am Schreibtisch vor orangefarbener Wand"></div>
    </article>
  </main>
</body>
</html>
```